High Tech Real Estate Startup needs a business card

We are developing an innovative real estate marketing product based around advanced search and virtual reality.

We talk to people, we need business cards.

Target Market(s)

The target market is technology professionals and realtors.

Contact Information for Business Card

The information to be included will include

Name
Title
Phone Number
E-mail Address
www.quelzo.com

It should use simple iconography for each one of those fields.

Font styles to use
Other font styles liked:
• Co, Jubilat, Avenir

Colors

Designer to choose colors to be used in the design.

Requirements
Must have
• Clean aesthetic,
• Good use of negative space.
• It should use our company logo, shown in the attached file. It is able to use the negative of that logo (coloured font and white background) and I have attached other acceptable accent colours in a swatch file.
Should not have
• Should not be too busy
• No extraneous text (slogans, tag lines etc)

```html
<!DOCTYPE html>
<html lang="en">
<head>
<meta charset="utf-8">
<title>Quelzo Business Card</title>
<link rel="stylesheet" href="https://fonts.googleapis.com/css2?family=Nunito+Sans:wght@400;600;700&display=swap">
<style>
  :root {
    --backdrop: #9e9e9e;
    --paper: #ffffff;
    --crimson: #bc2342;
    --ink: #2b2b2b;
  }
  * { margin: 0; padding: 0; box-sizing: border-box; }
  html, body {
    width: 1183px; height: 1200px; overflow: hidden;
    background: var(--backdrop);
    font-family: "Nunito Sans", "Avenir", sans-serif;
  }
  .canvas { position: relative; width: 1183px; height: 1200px; }
  .card { position: absolute; left: 128px; width: 927px; height: 533px; overflow: hidden; }
  .card--front { top: 43px; background: var(--paper); }
  .card--back { top: 623px; background: var(--crimson); }

  .brand-block {
    position: absolute; width: 306px; height: 163px;
    display: flex; align-items: center; justify-content: center;
    font-weight: 600; font-size: 58px; letter-spacing: 1px; line-height: 1;
  }
  .card--front .brand-block { left: 42px; top: 185px; background: var(--crimson); color: var(--paper); }
  .card--back .brand-block { left: 91px; top: 185px; background: var(--paper); color: var(--crimson); }

  .icon-rail {
    position: absolute; left: 411px; top: 84px; width: 77px; height: 364px;
    background: var(--crimson); border-radius: 38px;
  }
  .icon {
    position: absolute; left: 15px; width: 47px; height: 47px;
    background: var(--paper); border-radius: 50%;
    display: flex; align-items: center; justify-content: center;
  }
  .icon svg { width: 30px; height: 30px; }
  .icon--person { top: 29px; }
  .icon--phone { top: 114px; }
  .icon--mail { top: 200px; }
  .icon--web { top: 285px; }

  .contact { position: absolute; left: 513px; line-height: 1; color: var(--ink); white-space: nowrap; }
  .contact__name { top: 121px; font-size: 42px; font-weight: 600; color: var(--crimson); }
  .contact__title { top: 162px; font-size: 34px; font-weight: 600; }
  .contact__phone { top: 207px; font-size: 38px; font-weight: 600; }
  .contact__email { top: 292px; font-size: 38px; font-weight: 600; }
  .contact__web { top: 374px; font-size: 37px; font-weight: 700; }

  .web-tab {
    position: absolute; left: 488px; top: 229px; width: 439px; height: 76px;
    background: var(--paper); border-radius: 38px 0 0 38px;
    display: flex; align-items: center; padding-left: 35px;
    color: var(--crimson); font-size: 42px; font-weight: 700; line-height: 1;
  }
</style>
</head>
<body>
<div class="canvas">
  <section class="card card--front">
    <div class="brand-block">QUELZO</div>

    <div class="icon-rail">
      <span class="icon icon--person">
        <svg viewBox="0 0 30 30"><circle cx="15" cy="10" r="5.5" fill="#2b2b2b"/><path d="M5 25c0-6 4.5-9 10-9s10 3 10 9z" fill="#2b2b2b"/></svg>
      </span>
      <span class="icon icon--phone">
        <svg viewBox="0 0 30 30"><path d="M11 5l3 5-2.5 2c1 3 3 5.5 5.5 7l2-2.5 5 3-2 4c-8-1-14-8-15-16z" fill="#2b2b2b"/></svg>
      </span>
      <span class="icon icon--mail">
        <svg viewBox="0 0 30 30" fill="none" stroke="#2b2b2b" stroke-width="1.6"><rect x="3" y="7" width="24" height="16"/><path d="M3 7l12 10 12-10M3 23l9-8M27 23l-9-8"/></svg>
      </span>
      <span class="icon icon--web">
        <svg viewBox="0 0 30 30" fill="none" stroke="#2b2b2b" stroke-width="1.5"><circle cx="15" cy="15" r="11"/><ellipse cx="15" cy="15" rx="5" ry="11"/><path d="M4 15h22M6 9.5h18M6 20.5h18M15 4v22"/></svg>
      </span>
    </div>

    <div class="contact contact__name">NAME</div>
    <div class="contact contact__title">Title</div>
    <div class="contact contact__phone">Phone Number</div>
    <div class="contact contact__email">E-mail Address</div>
    <div class="contact contact__web">www.quelzo.com</div>
  </section>

  <section class="card card--back">
    <div class="brand-block">QUELZO</div>
    <div class="web-tab">www.quelzo.com</div>
  </section>
</div>
</body>
</html>
```